I need a new business card design for my pharmacy.

I need a business card design. I will include my logo.
The card needs to be readable. I prefer to have my logo on one side along with my website, the other side includes the other information. Please use combination of black, neon green, white, and silver. This needs to catch the eye but yet be clearly visible and legible. Thanks

Industry/Entity Type

Pharmacy

Contact Information for Business Card

It needs to have the following information listed:
Mel's Apothecary Owner/Pharm D.
7134 North Brook Lane
Sioux Falls, SD 57231
Phone 605-318-6207
Fax 605-318-6209
email: mel@melsapothecary-example.com
www.melsapothecary-example.com
Store hours Monday-Friday 8 am- 7 pm
Saturday 8 am- 12 pm
Sunday Closed
Please utilize the colors black, white, and neon green, maybe silver.

Requirements
Must have
• It needs to be easily readable!
Nice to have
• It should catch the eye.
Should not have
• Do not use any other colors except listed: black, neon green, white, & silver.

```html
<!DOCTYPE html>
<html lang="en">
<head>
<meta charset="utf-8">
<title>Mel's Apothecary – Business Card Front</title>
<link rel="stylesheet" href="https://fonts.googleapis.com/css2?family=Noto+Sans:wght@500&family=Open+Sans:wght@400&display=swap">
<style>
  :root {
    --silver-light: #f1f1f3;
    --silver-mid: #dcdde0;
    --silver-dark: #c6c7cb;
    --ink: #1a1a1a;
    --ink-soft: #5f6063;
    --neon: #9fd83a;
  }
  * { margin: 0; padding: 0; box-sizing: border-box; }
  html, body {
    width: 1200px;
    height: 686px;
    overflow: hidden;
    background: var(--silver-mid);
  }
  .card {
    position: relative;
    width: 1200px;
    height: 686px;
    overflow: hidden;
    background:
      radial-gradient(ellipse at 30% 20%, rgba(255,255,255,0.55), rgba(255,255,255,0) 60%),
      linear-gradient(135deg, var(--silver-mid) 0%, var(--silver-light) 45%, var(--silver-mid) 75%, var(--silver-dark) 100%);
  }
  .brand-mark {
    position: absolute;
    left: 150px;
    top: 300px;
    width: 120px;
    height: 120px;
  }
  .brand-divider {
    position: absolute;
    left: 383px;
    top: 266px;
    width: 3px;
    height: 188px;
    background: var(--ink);
  }
  .brand-name {
    position: absolute;
    left: 436px;
    top: 312px;
    font-family: "Noto Sans", sans-serif;
    font-weight: 500;
    font-size: 72px;
    line-height: 1;
    letter-spacing: -1px;
    color: var(--ink);
    white-space: nowrap;
  }
  .contact {
    position: absolute;
    bottom: 34px;
    font-family: "Open Sans", sans-serif;
    font-weight: 400;
    font-size: 23px;
    letter-spacing: 1.5px;
    color: var(--ink-soft);
    white-space: nowrap;
  }
  .contact--email { left: 38px; }
  .contact--web { right: 50px; }
</style>
</head>
<body>
  <main class="card">
    <svg class="brand-mark" viewBox="0 0 120 120" aria-hidden="true">
      <circle cx="60" cy="60" r="52" fill="var(--neon)"/>
    </svg>
    <div class="brand-divider"></div>
    <h1 class="brand-name">Mel's Apothecary</h1>
    <p class="contact contact--email">mel@melsapothecary-example.com</p>
    <p class="contact contact--web">www.melsapothecary-example.com</p>
  </main>
</body>
</html>
```